Brochure for Company

We need a standard trifold brochure or a square trifold brochure design. We are a home medical equipment company that specializes in pediatric as well as prenatal and postnatal medical equipment (www.vorantiq.com). We are owned by a home care company called Bluestem Home Health (www.bluestemnurse.com) which specializes in pediatric home care. Our two main products are breast pumps and nebulizer compressor kits. However, we also carry other respiratory as well as pre and post natal products. We are looking a creative and simple design. Most of our competitors brochures are very cookie cutter and too wordy so I want to stray away from them. The design should communicate that we care about our clients, meaning children and parents.

I have added a bunch of images that could be used. I also included the type of brochure I would ideally want to use.

Reason: i'm travelling the next couple of days so i need more time to review the submissions.

Industry/Entity Type

Medical

```html
<!DOCTYPE html>
<html lang="en">
<head>
<meta charset="utf-8">
<title>Vorantiq Trifold Brochure – Inside Pages</title>
<link rel="stylesheet" href="https://fonts.googleapis.com/css2?family=Marcellus&family=Open+Sans:wght@400;600;700&display=swap">
<style>
  :root {
    --navy: #1f3f7a;
    --blue: #2f5fa8;
    --blue-light: #3b6cb4;
    --orange: #e8742a;
    --ink: #4d4d4d;
    --muted: #7a7a7a;
    --paper: #ffffff;
    --panel-tint: #eef2f7;
    --backdrop: #8e8e8e;
    --pump-dark: #2a2a2a;
    --pump-light: #e9e4da;
    --neb-teal: #4bb3a6;
  }
  * { box-sizing: border-box; margin: 0; padding: 0; }
  html, body { width: 1200px; height: 1200px; overflow: hidden; }
  body {
    background: radial-gradient(circle at 50% 45%, #a3a3a3 0%, var(--backdrop) 70%);
    font-family: "Open Sans", Arial, sans-serif;
    color: var(--ink);
    position: relative;
  }
  .brochure {
    position: absolute;
    left: 50px; top: 175px;
    width: 1100px; height: 850px;
    display: grid;
    grid-template-columns: repeat(3, 1fr);
    background: var(--paper);
    box-shadow: 0 18px 40px rgba(0,0,0,.35);
  }
  .panel { position: relative; overflow: hidden; border-right: 1px solid #e2e2e2; }
  .panel:last-child { border-right: 0; }
  .panel--tinted { background: linear-gradient(160deg, #ffffff 0%, var(--panel-tint) 60%, #dfe6ef 100%); }

  .intro-bands { position: absolute; left: 0; top: 0; }
  .band-title { font-family: "Marcellus", Georgia, serif; fill: #fff; }
  .band-copy { font-family: "Open Sans", Arial, sans-serif; fill: var(--ink); font-size: 13px; }

  .page-tag {
    position: absolute; top: 26px; right: 24px;
    font-family: "Marcellus", Georgia, serif;
    font-size: 12px; color: var(--navy);
    border-bottom: 1px solid var(--navy); padding: 0 4px 2px;
  }

  .product { position: absolute; left: 22px; right: 20px; display: flex; gap: 16px; }
  .product-photo { flex: none; border-radius: 50%; }
  .product-photo--square { border-radius: 10px; }
  .product-body { flex: 1; }
  .product-title { font-size: 16px; font-weight: 600; color: var(--blue); line-height: 1.2; }
  .features-label { font-size: 15px; font-weight: 600; color: var(--orange); margin-top: 2px; }
  .feature-list { list-style: none; font-size: 13px; line-height: 1.55; color: var(--muted); }
  .product-copy { font-size: 12px; line-height: 1.55; color: var(--muted); }
  .config-label { font-size: 13px; font-weight: 600; color: var(--navy); margin: 2px 0; }

  .rule { position: absolute; left: 22px; right: 22px; height: 2px; background: var(--navy); }
  .section-note { position: absolute; left: 22px; right: 22px; }
  .section-label {
    display: inline-block; background: var(--navy); color: #fff;
    font-family: "Marcellus", Georgia, serif; font-size: 14px;
    padding: 3px 12px; margin-bottom: 8px;
  }
</style>
</head>
<body>
<main class="brochure">

  <section class="panel panel--intro">
    <svg class="intro-bands" width="367" height="390" viewBox="0 0 367 390">
      <g transform="translate(0,28) rotate(12.3)">
        <rect x="-20" y="0" width="420" height="52" fill="var(--navy)"/>
        <text class="band-title" x="22" y="37" font-size="30">Who We Are</text>
      </g>
      <g transform="translate(0,100) rotate(12.3)">
        <text class="band-copy" x="18" y="22">We are a home medical equipment provider for</text>
        <text class="band-copy" x="18" y="40">families, offering pediatric, prenatal and postnatal</text>
        <text class="band-copy" x="18" y="58">care products delivered with warmth and support.</text>
      </g>
      <g transform="translate(0,198) rotate(12.3)">
        <rect x="-20" y="0" width="420" height="44" fill="var(--navy)"/>
        <text class="band-title" x="22" y="32" font-size="26">Our Product</text>
        <rect x="-20" y="44" width="420" height="32" fill="var(--blue-light)"/>
        <text class="band-title" x="22" y="68" font-size="20">Breast Pumps</text>
      </g>
    </svg>

    <article class="product" style="top:420px;">
      <div class="product-photo" role="img" aria-label="Single manual breast pump product photo"
           style="width:112px;height:112px;background:radial-gradient(circle at 40% 40%, var(--pump-light), var(--pump-dark) 75%);"></div>
      <div class="product-body">
        <h3 class="product-title">Lunaro Single Manual Breast Pump</h3>
        <p class="features-label">Features</p>
        <ul class="feature-list">
          <li>Easy to use with one hand</li>
          <li>Quiet, discreet design</li>
          <li>Comfort-fit breast shield</li>
          <li>Includes bottle and stand</li>
        </ul>
      </div>
    </article>

    <article class="product" style="top:610px;">
      <div class="product-photo" role="img" aria-label="Double electric breast pump product photo"
           style="width:112px;height:112px;background:radial-gradient(circle at 45% 45%, var(--pump-light), var(--pump-dark) 70%);"></div>
      <div class="product-body">
        <h3 class="product-title">Lunaro Personal Double Electric Breastpump</h3>
        <p class="features-label">Features</p>
        <ul class="feature-list">
          <li>Single or double pumping</li>
          <li>Double pumping saves time</li>
          <li>Personalized adjustments</li>
          <li>Two-phase suction pattern</li>
          <li>Power adapter</li>
        </ul>
      </div>
    </article>
  </section>

  <section class="panel panel--middle">
    <span class="page-tag">page 1 of 2</span>

    <article class="product" style="top:70px;">
      <div class="product-photo product-photo--square" role="img" aria-label="Electric breast pump kit product photo"
           style="width:92px;height:92px;background:linear-gradient(145deg,#f4f4f4,#c9ccd2);"></div>
      <div class="product-body">
        <h3 class="product-title">Corvela Electric Breast Pump</h3>
        <p class="features-label">Features</p>
        <p class="product-copy">Hospital-strength suction in a compact, lightweight unit. Adjustable speed and vacuum settings. Quiet motor for night feedings. Closed system keeps milk clean.</p>
      </div>
    </article>

    <article class="product" style="top:260px;">
      <div class="product-photo product-photo--square" role="img" aria-label="Portable breast pump with bottles product photo"
           style="width:92px;height:92px;background:linear-gradient(145deg,#fafafa,#cfd6de);"></div>
      <div class="product-body">
        <h3 class="product-title">Corvela Softline Breast Pump</h3>
        <p class="features-label">Features</p>
        <p class="product-copy">Three suction settings for comfort. Runs on batteries or wall power. Easy to clean parts. Fits in a small tote.</p>
      </div>
    </article>

    <div class="rule" style="top:440px;"></div>

    <div class="section-note" style="top:462px;">
      <span class="section-label">Nebulizers</span>
      <p class="product-copy">Our nebulizer compressor kits are carefully chosen from trusted makers to deliver gentle, effective breathing treatments at home for children and adults alike.</p>
    </div>
  </section>

  <section class="panel panel--tinted">
    <span class="page-tag">page 3 of 4</span>

    <article class="product" style="top:70px;">
      <div class="product-photo" role="img" aria-label="Portable nebulizer compressor product photo"
           style="width:84px;height:84px;background:radial-gradient(circle at 45% 45%, #d9f0ec, var(--neb-teal) 80%);"></div>
      <div class="product-body">
        <h3 class="product-title">Aerolen Roamer Personal Delivery System</h3>
        <p class="config-label">Standard Configuration:</p>
        <p class="product-copy">A compact compressor with a reusable nebulizer, tubing and carry bag. Weighs under two pounds.</p>
      </div>
    </article>

    <div class="product-photo product-photo--square" role="img" aria-label="Nebulizer carry bag and accessories product photo"
         style="position:absolute;left:130px;top:215px;width:150px;height:110px;background:linear-gradient(160deg,#f3efe6,#cfe3ea);"></div>

    <article class="product" style="top:345px;">
      <div class="product-body">
        <p class="config-label">Aerolen Portability:</p>
        <p class="product-copy">Rechargeable battery for on-the-go care. Works with all Aerolen reusable nebulizers.</p>
      </div>
    </article>

    <div class="rule" style="top:440px;"></div>

    <article class="product" style="top:462px;">
      <div class="product-photo" role="img" aria-label="Compressor with reusable nebulizer product photo"
           style="width:84px;height:84px;background:radial-gradient(circle at 45% 45%, #ffffff, #aeb7c2 80%);"></div>
      <div class="product-body">
        <h3 class="product-title">Aerolen Calma Compressor and Reusable Nebulizer</h3>
        <p class="config-label">Standard Configuration:</p>
        <p class="product-copy">Pediatric mask and mouthpiece included. Durable compressor built for daily use. Fast treatment times for busy families.</p>
      </div>
    </article>
  </section>

</main>
</body>
</html>
```